Tess Marlowe Communication business card

I am starting a small, country-based business that offers writing, communication and marketing services to a wide range of clients, inner city big business, to mining, through to agriculture.

The appeal of my business is that it's mobile and flexible. It's just me, with lots of hands-on experience on construction and infrastructure projects.

I can provide the following services:

• Communication planning and management
• Issues and media management
• Marketing and communication materials
• Project management and strategy
• Government liaison
• Incident management communication
• Stakeholder management

It would be great to be able to use the elements of the business card design on other stationery.

Industry/Entity Type

Communication

Requirements
Must have
• The following information:

Tess Marlowe
M: 0427 391 864
E: tess@tmcommsmail.com

PO Box 152
Durrandale Q 4472
Nice to have
• a rural element (windmill, workboots, wheat stalk)

```html
<!DOCTYPE html>
<html lang="en">
<head>
<meta charset="utf-8">
<title>Tess Marlowe Communications – Business Card</title>
<link rel="stylesheet" href="https://fonts.googleapis.com/css2?family=EB+Garamond:wght@600;700&display=swap">
<style>
  :root {
    --card-deep: #0a46a6;
    --card-mid: #1f4fd6;
    --card-glow: #3f66f4;
    --lower-band: rgba(8, 40, 140, 0.18);
    --frame-line: #0b1f3f;
    --rule-line: rgba(170, 195, 255, 0.55);
    --title-ink: #c9d5f3;
    --service-ink: #a9b9ea;
    --contact-ink: #d4dcf3;
    --mill-light: rgba(200, 215, 250, 0.55);
    --mill-soft: rgba(160, 185, 245, 0.15);
  }
  * { margin: 0; padding: 0; box-sizing: border-box; }
  html, body {
    width: 1200px;
    height: 720px;
    overflow: hidden;
    background: var(--card-deep);
  }
  .card {
    position: relative;
    width: 1200px;
    height: 720px;
    overflow: hidden;
    font-family: "EB Garamond", Garamond, Georgia, serif;
    background:
      radial-gradient(ellipse 55% 60% at 52% 48%, var(--card-glow) 0%, var(--card-mid) 45%, var(--card-deep) 100%);
  }
  .lower-band {
    position: absolute;
    left: 0; right: 0; top: 496px; bottom: 0;
    background: var(--lower-band);
  }
  .band-rule {
    position: absolute;
    left: 0; right: 0; top: 494px;
    height: 3px;
    background: var(--rule-line);
  }
  .frame {
    position: absolute;
    border: 2px solid var(--frame-line);
  }
  .frame--outer { left: 38px; top: 38px; width: 1124px; height: 643px; }
  .frame--inner { left: 69px; top: 67px; width: 1062px; height: 585px; }

  .windmill-art {
    position: absolute;
    left: 55px; top: 117px;
    width: 302px; height: 379px;
    background:
      radial-gradient(ellipse 50% 50% at 50% 35%, var(--mill-light) 0%, var(--mill-soft) 70%, transparent 100%);
    border-radius: 6px;
  }

  .business-name {
    position: absolute;
    right: 77px; top: 62px;
    font-size: 67px;
    font-weight: 700;
    color: var(--title-ink);
    white-space: nowrap;
    letter-spacing: 0.3px;
    text-shadow: 3px 3px 3px rgba(0, 10, 40, 0.7);
  }

  .services { list-style: none; }
  .services li {
    position: absolute;
    font-size: 28px;
    font-weight: 600;
    color: var(--service-ink);
    white-space: nowrap;
    line-height: 1;
  }
  .services li::before {
    content: "";
    position: absolute;
    left: -31px; top: 11px;
    width: 7px; height: 7px;
    border-radius: 50%;
    background: var(--service-ink);
  }
  .services .s1 { left: 504px; top: 207px; }
  .services .s2 { left: 543px; top: 246px; }
  .services .s3 { left: 559px; top: 284px; }
  .services .s4 { left: 543px; top: 323px; }
  .services .s5 { left: 504px; top: 361px; }

  .person-name {
    position: absolute;
    right: 76px; top: 500px;
    font-size: 68px;
    font-weight: 700;
    color: var(--title-ink);
    white-space: nowrap;
    text-shadow: 3px 3px 3px rgba(0, 10, 40, 0.6);
  }

  .contact, .postal {
    position: absolute;
    font-size: 28px;
    font-weight: 700;
    color: var(--contact-ink);
    line-height: 40px;
    white-space: nowrap;
  }
  .contact { left: 83px; top: 570px; }
  .postal { right: 76px; top: 570px; text-align: right; }
</style>
</head>
<body>
  <div class="card">
    <div class="lower-band"></div>
    <div class="band-rule"></div>
    <div class="frame frame--outer"></div>
    <div class="frame frame--inner"></div>

    <div class="windmill-art" role="img" aria-label="Line illustration of a traditional windmill with four lattice sails"></div>

    <h1 class="business-name">Tess Marlowe Communications</h1>

    <ul class="services">
      <li class="s1">Communication planning and management</li>
      <li class="s2">Issues and media management</li>
      <li class="s3">Project management and strategy</li>
      <li class="s4">Government liaison</li>
      <li class="s5">Stakeholder management</li>
    </ul>

    <h2 class="person-name">Tess Marlowe</h2>

    <div class="contact">
      <p>M: 0427 391 864</p>
      <p>E: tess@tmcommsmail.com</p>
    </div>

    <div class="postal">
      <p>PO Box 152</p>
      <p>Durrandale Q 4472</p>
    </div>
  </div>
</body>
</html>
```